Book cover for book about Climate Change

Looking for a clean, bold, and attractive cover for a mass-market paperback (5.5"x 8.5") about solving the climate change problem. Title is either "Where the Rivers Begin” or A Garden Left Standing” (your choice), subtitle is "A five-step plan to reverse climate change — to ensure that your grandchildren will live on a clean and comfortable planet," author is Milo Pardrey. Thinking that it *might* feature an image of Earth (or a portion thereof) and its very thin layer of atmosphere -- but STRONGLY encourage other ideas too!

Requirements
Nice to have
• Keep it positive — NOT scary doom-and-gloom

```html
<!DOCTYPE html>
<html lang="en">
<head>
<meta charset="utf-8">
<title>Where the Rivers Begin — Book Cover</title>
<link rel="stylesheet" href="https://fonts.googleapis.com/css2?family=Montserrat:wght@700;800;900&display=swap">
<style>
  :root {
    --page-bg: #e6e6e6;
    --cover-bg: #dfe3ea;
    --cover-mist: #eef1f5;
    --ink-indigo: #2c2878;
    --ink-green: #1f8a3c;
    --ink-yellow: #d8c42a;
    --leaf-green: #2f9a3a;
    --snow: #f2f4f7;
    --rock: #3f6f8c;
  }
  * { margin: 0; padding: 0; box-sizing: border-box; }
  html, body {
    width: 1200px;
    height: 960px;
    overflow: hidden;
    background: var(--page-bg);
  }
  .canvas {
    position: relative;
    width: 1200px;
    height: 960px;
  }
  .cover {
    position: absolute;
    left: 344px;
    top: 107px;
    width: 512px;
    height: 746px;
    background: linear-gradient(180deg, var(--cover-bg) 0%, var(--cover-mist) 55%, var(--snow) 100%);
    overflow: hidden;
    font-family: "Montserrat", sans-serif;
    text-align: center;
  }
  .cover-landscape {
    position: absolute;
    left: 0;
    right: 0;
    bottom: 0;
    height: 330px;
  }
  .cover-landscape svg { display: block; width: 100%; height: 100%; }
  .title {
    position: absolute;
    top: 44px;
    left: 0;
    right: 0;
    font-weight: 900;
    font-size: 96px;
    line-height: 111px;
    letter-spacing: -3px;
    text-transform: uppercase;
    background: linear-gradient(115deg,
      var(--ink-indigo) 0%, var(--ink-indigo) 18%,
      var(--leaf-green) 30%, var(--ink-yellow) 38%,
      var(--ink-indigo) 48%, var(--leaf-green) 60%,
      var(--ink-indigo) 72%, var(--ink-yellow) 80%,
      var(--ink-indigo) 90%, #15133a 100%);
    -webkit-background-clip: text;
    background-clip: text;
    color: transparent;
  }
  .title-line { display: block; }
  .subtitle {
    position: absolute;
    top: 475px;
    left: 40px;
    right: 40px;
    color: var(--ink-green);
    font-weight: 700;
    font-size: 12.5px;
    line-height: 25px;
    text-transform: uppercase;
    letter-spacing: -0.2px;
  }
  .author {
    position: absolute;
    bottom: 16px;
    left: 0;
    right: 0;
    color: var(--ink-indigo);
    font-weight: 800;
    font-size: 25px;
    letter-spacing: -0.5px;
    text-transform: uppercase;
  }
</style>
</head>
<body>
<main class="canvas">
  <section class="cover">
    <div class="cover-landscape" role="img" aria-label="Snow-covered mountain range under a pale misty sky">
      <svg viewBox="0 0 512 330" preserveAspectRatio="none">
        <defs>
          <linearGradient id="mountainTone" x1="0" y1="0" x2="0" y2="1">
            <stop offset="0" stop-color="#eef1f5" stop-opacity="0"/>
            <stop offset="0.35" stop-color="#c9d7e2" stop-opacity="0.6"/>
            <stop offset="0.6" stop-color="#7fa2b8" stop-opacity="0.55"/>
            <stop offset="1" stop-color="#f2f4f7" stop-opacity="0.9"/>
          </linearGradient>
        </defs>
        <rect width="512" height="330" fill="url(#mountainTone)"/>
      </svg>
    </div>

    <h1 class="title">
      <span class="title-line">Where</span>
      <span class="title-line">The</span>
      <span class="title-line">Rivers</span>
      <span class="title-line">Begin</span>
    </h1>

    <p class="subtitle">A five-step plan to reverse climate change – to ensure that your grandchildren will live on a clean and comfortable planet</p>

    <p class="author">Milo Pardrey</p>
  </section>
</main>
</body>
</html>
```